i would like a business card to leave with customers and potential customers for electrical work and for the supply and install of reverse cycle airconditioning in the domestic and commercial market.
I own my own business and im a sole trader. I have an a'class electrical lisence and also a refrigeration lisence so i am
able to offer complete installations in airconditioning by a fully qualified and lisenced tradesman.
im looking for something that comes across as unique and professional.
i had the coluor black and some gold in mind but open to any coluors.
something like Beacon Electrical & Refrigeration
or Beacon Air.
i will use this design on a business card to advertise through summer to help generate installs through the busy season.

Target Market(s)

Mainly domestic house holds through summer who are in need of airconditioning and reliable information to acomadate thier cooling and heating requirements

Industry/Entity Type

Electrical

Requirements
Must have
• Business name- Beacon
My name- Peter Wollaston
My mobile no- 0457 819 302
My email- prwollaston@tarvel.com.au
Installation & Decomissioning of aiconditioning split systems
LIC NO: KTR 407516
Nice to have
• Beacon Electrical & Refrigeration

```html
<!DOCTYPE html>
<html lang="en">
<head>
<meta charset="utf-8">
<title>Beacon Electrical &amp; Refrigeration – Business Card</title>
<link rel="stylesheet" href="https://fonts.googleapis.com/css2?family=Aldrich&family=Oswald:wght@700&display=swap">
<style>
  :root {
    --page: #ffffff;
    --card: #000000;
    --ink: #ffffff;
    --gold: #c9b22a;
    --gold-dark: #6b5a10;
    --badge-top: #00ffff;
    --badge-bottom: #99ff00;
  }
  html, body {
    margin: 0;
    padding: 0;
    width: 1200px;
    height: 819px;
    overflow: hidden;
    background: var(--page);
  }
  .canvas {
    position: relative;
    width: 1200px;
    height: 819px;
  }
  .card {
    position: absolute;
    left: 118px;
    top: 134px;
    right: 0;
    bottom: 0;
    background: var(--card);
    color: var(--ink);
    font-family: "Aldrich", sans-serif;
  }
  .brand {
    position: absolute;
    left: 70px;
    top: 52px;
    width: 170px;
    text-align: center;
  }
  .brand-mark {
    display: block;
    width: 96px;
    height: 96px;
    margin: 0 auto 14px;
    background: var(--gold);
  }
  .brand-name {
    font-family: "Aldrich", sans-serif;
    font-size: 38px;
    color: var(--gold);
    line-height: 1;
  }
  .badge {
    position: absolute;
    left: 885px;
    top: 52px;
  }
  .holder {
    position: absolute;
    left: 0;
    right: 0;
    top: 268px;
    text-align: center;
  }
  .holder-name {
    margin: 0 0 0 55px;
    font-size: 84px;
    font-weight: 400;
    letter-spacing: 2px;
    line-height: 1;
  }
  .holder-licence {
    margin: 10px 0 0 55px;
    font-size: 33px;
    letter-spacing: 1px;
  }
  .business-name {
    margin: 8px 0 0 55px;
    font-family: "Oswald", sans-serif;
    font-weight: 700;
    font-size: 38px;
    line-height: 1.1;
    background: linear-gradient(90deg, var(--gold-dark), var(--gold) 45%, var(--gold-dark));
    -webkit-background-clip: text;
    background-clip: text;
    color: transparent;
  }
  .contact {
    position: absolute;
    left: 0;
    right: 0;
    top: 537px;
    text-align: center;
    font-size: 26px;
    line-height: 31px;
    letter-spacing: 0.5px;
  }
  .contact p { margin: 0 0 0 55px; }
  .contact .gap { display: inline-block; width: 22px; }
</style>
</head>
<body>
<div class="canvas">
  <section class="card">
    <div class="brand">
      <span class="brand-mark"></span>
      <div class="brand-name">Beacon</div>
    </div>

    <svg class="badge" width="126" height="152" viewBox="0 0 126 152" aria-label="Authorised trade badge">
      <defs>
        <linearGradient id="badgeFill" x1="0" y1="0" x2="0" y2="1">
          <stop offset="0" stop-color="var(--badge-top)"/>
          <stop offset="1" stop-color="var(--badge-bottom)"/>
        </linearGradient>
      </defs>
      <rect x="0" y="0" width="126" height="126" fill="url(#badgeFill)"/>
    </svg>

    <div class="holder">
      <h1 class="holder-name">Peter Wollaston</h1>
      <div class="holder-licence">(A'Class Electrical &amp; Refrigeration Liscense)</div>
      <div class="business-name">Beacon Electrical &amp; Refrigeration</div>
    </div>

    <div class="contact">
      <p>Mob:&nbsp; 0457 819 302<span class="gap"></span>Email:&nbsp; prwollaston@tarvel.com.au</p>
      <p>Installation &amp; Decommissioning of Airconditioning Split Systems</p>
      <p>LIC NO:&nbsp; KTR 407516</p>
    </div>
  </section>
</div>
</body>
</html>
```